Bellmont Crestwood Engraving Awards

I want an ecommerce site where customers can review our in stock items and or select from our vendor on-line catalog when placing an order. I also need a place where they can enter the inscription information for each award. Will accept Coinvale payments. Also need a section for perpetual awards where they sign up for the monthly awards, they select the Master Plaque they want and also select the monthly award they want. Has to be for single awards or multi awards from a single customer. Current web site is www.TopLaurelTrophy.com and I need to keep the same address. You can review it for what we do but it’s old and done by "me".
The main focus of our sales are perpetual awards so that should be front and center on the main page. I would like the customer to enter their information on an order form and select the Mater Plaque and which Monthly they would like. They can also do a monthly without a Master Plaque. Once the order is submitted, I would like to receive an email message with all the information in the text of the email.
I am in the process of getting newer pictures of these items and they should be available by the end of the week if not sooner.
I would like the links to the catalogs to also be on the home page.
An “Ask a Question” would also me a good idea where they inter contact information, enter their question and I receive an email with their questions and information for my reply to them.
Our key phrase is “The Power of Thank You!” We would like to see this on every page and where ever you think it would apply. We sell to many different companies and organizations all over the United States.

Target Market(s)

Auto Dealers, Real Estate Brokers, Sales Organizations

Coding

Coded - Design and coding required

Number of Pages Required

4 page

Colors
0355a3
ec1f27
fbed22
f78f20
a54499

Requirements
Must have
• Perpetual Plaque with Monthly Awards
• On-Line ordering process with select buttons for the Master Plaque and which monthly.
• Place to enter inscription for award
• Links to my suppliers catalog - like on my current site. A way to order from the catalog and pay with Coinvale.
Nice to have
• search engine that would allow search of vendors catalog
• A section for sports and academic awards

```html
<!DOCTYPE html>
<html lang="en">
<head>
<meta charset="utf-8">
<title>Catalog Order – Bellmont Crestwood Engraving Awards</title>
<link href="https://fonts.googleapis.com/css2?family=Open+Sans:wght@400;600;700&family=Raleway:wght@300;400;500;600&display=swap" rel="stylesheet">
<style>
:root{
  --pink:#e4215f;
  --pink-dark:#d81c55;
  --orange:#f29a14;
  --ink:#1d1d1d;
  --grey:#555;
  --line:#d5d5d5;
  --footer:#1f1f1f;
  --footer-base:#141414;
  --footer-text:#b9b9b9;
}
*{margin:0;padding:0;box-sizing:border-box}
html,body{width:867px;height:1200px;overflow:hidden;background:#fff}
body{position:relative;font-family:"Open Sans",Arial,sans-serif;color:var(--ink)}
.abs{position:absolute}

.topbar{left:0;top:0;width:867px;height:22px;background:var(--pink)}
.topbar-links{position:absolute;right:62px;top:0;height:22px;display:flex;font-size:8.5px;color:#fff;align-items:center}
.topbar-links span{padding:0 12px;border-left:1px solid rgba(255,255,255,.35);line-height:22px}
.topbar-links span:first-child{border-left:0}

.header{left:0;top:22px;width:867px;height:70px;background:#fff}
.brand{position:absolute;left:70px;top:25px;display:flex;align-items:center;gap:6px;font-size:10.5px;color:#222;font-weight:400;letter-spacing:.2px}
.brand-dot{width:9px;height:9px;border-radius:50%;background:var(--pink)}
.nav{position:absolute;left:318px;top:30px;display:flex;gap:0;font-size:8.8px;font-weight:600;color:#333}
.nav a{margin-right:23px;text-decoration:none;color:inherit}
.nav a.active{border-bottom:2px solid var(--orange);padding-bottom:3px}
.nav-icon{position:absolute;top:25px;width:21px;height:21px;border-radius:50%}

.hero{left:0;top:92px;width:867px;height:255px;background:linear-gradient(90deg,#eef2f6 0%,#e9dcd2 45%,#dfe6ec 75%,#c9ced4 100%)}
.hero-title{position:absolute;left:72px;top:127px;font-family:Raleway,sans-serif;font-weight:500;font-size:29px;color:#111;letter-spacing:.5px}

.page-title{left:76px;top:390px;font-family:Raleway,sans-serif;font-weight:300;font-size:29px;color:var(--pink)}
.form-box{left:71px;top:448px;width:693px;height:327px;border:1px solid #cfcfcf}
.form-title{left:103px;top:474px;font-family:Raleway,sans-serif;font-size:19px;color:var(--orange)}
.field{position:absolute;height:28px;border:1.5px solid var(--line);font-size:10.5px;color:#777;padding-left:12px;line-height:25px;background:#fff}
.contact-email{left:424px;top:664px;font-size:10px;color:#444}
.pay{position:absolute;top:664px;width:23px;height:14px;border:1px solid #ddd;font-size:5px;font-weight:700;color:#3a5aa8;text-align:center;line-height:12px;background:#fff}
.submit{left:98px;top:709px;width:297px;height:41px;background:var(--pink);color:#fff;font-family:Raleway,sans-serif;font-weight:500;font-size:15.5px;text-align:center;line-height:41px}

.promo-left{left:0;top:856px;width:438px;height:89px;background:var(--pink-dark)}
.promo-right{left:438px;top:856px;width:429px;height:89px;background:var(--pink)}
.ship-1{left:181px;top:873px;font-size:20px;font-weight:700;color:#fff;letter-spacing:.3px}
.ship-2{left:181px;top:900px;font-size:16px;color:#fff}
.news{left:456px;top:872px;font-size:14.5px;color:#fff;font-weight:400}
.news b{font-weight:700}
.news-input{left:458px;top:898px;width:211px;height:27px;background:#fff;font-size:9px;font-style:italic;color:#999;padding-left:12px;line-height:27px}
.news-btn{left:673px;top:898px;width:101px;height:27px;background:var(--orange);color:#fff;font-size:10px;font-weight:700;text-align:center;line-height:27px}

.footer{left:0;top:945px;width:867px;height:213px;background:var(--footer)}
.footer-col{position:absolute;top:980px}
.footer-col h4{font-size:11.5px;font-weight:600;color:#fff;padding-bottom:10px;border-bottom:1px solid #444;width:110px;margin-bottom:12px}
.footer-col li{list-style:none;font-size:9.5px;color:var(--footer-text);line-height:19.5px;position:relative;padding-left:29px}
.footer-col li::before{content:"»";position:absolute;left:0;color:#fff;font-weight:700}
.base{left:0;top:1158px;width:867px;height:42px;background:var(--footer-base)}
.copyright{left:78px;top:1173px;font-size:9.5px;color:#aaa}
.base-pay{position:absolute;top:1170px;width:29px;height:18px;background:#fff;border-radius:2px;font-size:5.5px;font-weight:700;color:#2d4f9e;text-align:center;line-height:18px}
</style>
</head>
<body>

<div class="abs topbar">
  <div class="topbar-links"><span>My Account</span><span>Checkout</span><span>Blog</span><span>Log In</span><span>Call Today: 555-013-4820</span></div>
</div>

<div class="abs header">
  <div class="brand"><span class="brand-dot"></span>Bellmont Crestwood Engraving Awards</div>
  <nav class="nav"><a>HOME</a><a>SHOP</a><a>CATEGORIES</a><a>AWARDS</a><a>BLOG</a><a>ABOUT US</a><a class="active">CONTACT US</a></nav>
  <svg class="nav-icon" style="left:745px;background:var(--pink)" viewBox="0 0 21 21"><path d="M5 6h2l2 7h6l1.5-5H8" fill="none" stroke="#fff" stroke-width="1.6"/><circle cx="10" cy="15.5" r="1" fill="#fff"/><circle cx="14.5" cy="15.5" r="1" fill="#fff"/></svg>
  <svg class="nav-icon" style="left:773px;background:var(--orange)" viewBox="0 0 21 21"><circle cx="11.5" cy="9" r="3.6" fill="none" stroke="#fff" stroke-width="1.8"/><path d="M9 11.8 6 15" stroke="#fff" stroke-width="2" stroke-linecap="round"/></svg>
</div>

<div class="abs hero" role="img" aria-label="Photo of a smiling customer service agent wearing a headset, with a colleague at a monitor">
  <div class="hero-title">CATALOG ORDER</div>
</div>

<h1 class="abs page-title">Catalog Order</h1>
<div class="abs form-box"></div>
<h2 class="abs form-title">Order from Catalog Form</h2>

<div class="field" style="left:100px;top:511px;width:601px">Full Name</div>
<div class="field" style="left:100px;top:546px;width:146px">Email address</div>
<div class="field" style="left:251px;top:546px;width:147px">Price of Award</div>
<div class="field" style="left:405px;top:546px;width:146px">Contact Name</div>
<div class="field" style="left:555px;top:546px;width:146px">Tittle</div>
<div class="field" style="left:100px;top:583px;width:296px">Company Name</div>
<div class="field" style="left:404px;top:583px;width:145px">Quantity of Awards</div>
<div class="field" style="left:553px;top:583px;width:146px">Order type</div>
<div class="field" style="left:100px;top:621px;width:296px">Program Type</div>
<div class="field" style="left:405px;top:621px;width:296px">Billing Address:</div>
<div class="field" style="left:101px;top:661px;width:146px">Date</div>
<div class="field" style="left:251px;top:661px;width:147px">Code</div>

<div class="abs contact-email">Sales@TopLaurelTrophy.com</div>
<div class="pay" style="left:589px">Vero</div>
<div class="pay" style="left:619px">Altus</div>
<div class="pay" style="left:650px">Norda</div>
<div class="pay" style="left:680px">Merix</div>
<div class="pay" style="left:711px;width:25px">Coinvale</div>

<div class="abs submit">SUBMIT NOW</div>

<div class="abs promo-left"></div>
<div class="abs promo-right"></div>
<svg class="abs" style="left:121px;top:880px" width="48" height="40" viewBox="0 0 48 40">
  <rect x="13" y="2" width="33" height="24" rx="2" fill="#fff"/>
  <path d="M12 10H6L1 18v10h11z" fill="#fff"/>
  <path d="M4 18l3-5h4v5z" fill="#d81c55"/>
  <circle cx="9" cy="32" r="5" fill="#fff" stroke="#d81c55" stroke-width="2"/>
  <circle cx="36" cy="32" r="5" fill="#fff" stroke="#d81c55" stroke-width="2"/>
</svg>
<div class="abs ship-1">FREE SHIPPING FOR</div>
<div class="abs ship-2">ORDERS OVER $100</div>
<div class="abs news"><b>KEEP UPDATED.</b> SUBSCRIBE TO OUR NEWSLETTER!</div>
<div class="abs news-input">Enter Email Address</div>
<div class="abs news-btn">SUBSCRIBE</div>

<div class="abs footer"></div>
<div class="footer-col" style="left:79px"><h4>INFORMATION</h4><ul><li>Home</li><li>About us</li><li>Products</li><li>Blog</li><li>Contact us</li></ul></div>
<div class="footer-col" style="left:270px"><h4>SHOPPING GUIDE</h4><ul><li>FAQs</li><li>Payment</li><li>Shipment</li><li>Where is my order?</li><li>Return policy</li></ul></div>
<div class="footer-col" style="left:478px"><h4>MY ACCOUNT</h4><ul><li>My orders</li><li>My merchandise returns</li><li>My credit slips</li><li>My addresses</li><li>My personal info</li></ul></div>
<div class="footer-col" style="left:685px"><h4>SOCIAL MEDIA LINKS</h4><ul><li>Socialpage</li><li>Chatline</li><li>Worknet</li><li>Circleup</li><li>Clipcast</li></ul></div>

<div class="abs base"></div>
<div class="abs copyright">Copyright © 2016 Bellmont Crestwood Engraving Awards All rights reserved.</div>
<div class="base-pay" style="left:603px">Vero</div>
<div class="base-pay" style="left:642px">Altus</div>
<div class="base-pay" style="left:681px">Norda</div>
<div class="base-pay" style="left:720px">Merix</div>
<div class="base-pay" style="left:759px">Coinvale</div>

</body>
</html>
```